Cover for Where the Quiet River Bends Beyond Our Morning

Cover for a book that describes everything that happens to a person, from pre-birth life plans through growing in compassion and wisdom to death and living in the afterlife. The information is revealed in messages from people living in the life after this life. The title is Lanterns Along the Hidden Stair of Every Soul: Gathered from Voices Dwelling in the Further Meadow. Author is T. Morven Ashdale. Book size is 6 by 9.

Target Market(s)

General

Font styles to use
Serif

```html
<!DOCTYPE html>
<html lang="en">
<head>
<meta charset="utf-8">
<title>Lanterns Along the Hidden Stair of Every Soul — T. Morven Ashdale</title>
<link rel="stylesheet" href="https://fonts.googleapis.com/css2?family=Cinzel:wght@400;500&display=swap">
<style>
  :root {
    --sky-gold: #c9b95a;
    --moss: #8fa64a;
    --sea-teal: #2f7a78;
    --deep-teal: #17494c;
    --glow: #fffdf2;
    --title-white: #ffffff;
    --subtitle-gold: #f6d21a;
    --shadow: rgba(40, 40, 10, 0.55);
  }
  html, body {
    margin: 0;
    padding: 0;
    width: 800px;
    height: 1200px;
    overflow: hidden;
    background: var(--deep-teal);
  }
  .cover {
    position: relative;
    width: 800px;
    height: 1200px;
    overflow: hidden;
    font-family: "Cinzel", "Trajan Pro", serif;
  }
  .cover-art {
    position: absolute;
    inset: 0;
    background:
      radial-gradient(circle at 410px 600px, var(--glow) 0, rgba(255,253,235,0.85) 90px, rgba(220,225,190,0.35) 200px, rgba(0,0,0,0) 330px),
      linear-gradient(180deg, var(--sky-gold) 0%, var(--moss) 38%, var(--sea-teal) 68%, var(--deep-teal) 100%);
  }
  .title {
    position: absolute;
    top: 40px;
    left: 0;
    right: 0;
    margin: 0;
    text-align: center;
    color: var(--title-white);
    font-weight: 400;
    font-size: 72px;
    line-height: 88px;
    letter-spacing: 1px;
    text-shadow: 0 0 14px var(--shadow), 2px 3px 6px var(--shadow);
  }
  .title-line { display: block; }
  .subtitle {
    position: absolute;
    top: 862px;
    left: 0;
    right: 0;
    margin: 0;
    text-align: center;
    color: var(--subtitle-gold);
    font-weight: 400;
    font-size: 38px;
    line-height: 52px;
    letter-spacing: 0.5px;
    text-shadow: 2px 2px 4px rgba(0, 0, 0, 0.6);
  }
  .subtitle-line { display: block; }
  .author {
    position: absolute;
    top: 1090px;
    left: 0;
    right: 0;
    margin: 0;
    text-align: center;
    color: var(--title-white);
    font-weight: 400;
    font-size: 46px;
    letter-spacing: 1px;
    text-shadow: 2px 2px 5px rgba(0, 0, 0, 0.45);
  }
</style>
</head>
<body>
  <main class="cover">
    <div class="cover-art" role="img" aria-label="Illustration of a glowing spiral tunnel of light in gold, green and teal, with the silhouettes of an unborn child and a floating adult drifting toward the bright centre among faint stars"></div>
    <h1 class="title">
      <span class="title-line">Lanterns Along</span>
      <span class="title-line">the Hidden Stair</span>
      <span class="title-line">of Every</span>
      <span class="title-line">Soul:</span>
    </h1>
    <p class="subtitle">
      <span class="subtitle-line">Gathered from Voices</span>
      <span class="subtitle-line">Dwelling in the Further Meadow.</span>
    </p>
    <p class="author">T. Morven Ashdale</p>
  </main>
</body>
</html>
```